Brochure/flyer for Cloth Nappy Company

My Business name is Willow Dapplez Nappies
I am wanting a A4 size brochure (Flyer) to be folded twice. Measurements when folded 210 x 99 mm
I am just about to launch my Modern Cloth Nappy Products and i am wanting a brochure to target new mum's who aren't familiar with Modern cloth nappies and also for mums who are familiar with modern cloth nappies but are looking at trying my brand.
I want the Brochure to be very informative but yet Simple to read. I want people to feel like they want to buy my nappies after they read my Brochure.
The Brochure can be reworded and additional information can be added if you feel its needed, But i would like all the information listed below to be on the brochure.

MOTO: Cloth Nappies The Modern Way

The nappy design is designed in Australia and Australian Owned.

WHY USE CLOTH?
-Save thousands of Dollars
-Easy to use
-Looks Cute
-Super Absorbency
It costs approximately $3000 to use disposable nappies on a child from birth until 2 and a half years, that is Approximately 6000 nappies going into Landfill. This is based on a child going through 6-8 nappies per day.
Modern cloth nappies, on the other hand, cost around $500 for a full stash of 24 nappies. This allows for the child to wear 6-8 nappies per day with a load of nappies going in the wash every 2-3 days. As we have a range of nappies that are one-size-fits-most for bubs ranging from 3kg to 18kg, that $500 would cover your complete stash from birth right through to toilet training, Not to mention the money you would save by using the nappies again for any subsequent Children you may have.
Eliminates your baby's exposure to harmful Chemicals that can be in disposable nappies.
The manufacturing and use of disposable nappies can amount to 2-3 times more wasted water than using cloth nappies
Using Disposable Nappies fill up our landfill, Disposable nappies take more than 100 years to decompose, possibly up to 500 years.

PRODUCTS AVAILABLE:
Newborn: All in One (AIO) Fits approx 2-7kg
Velcro All in Two, One size Fits Most (OSFM) fits approx 3 to 18kg
Snap All in Two, One size Fits Most (OSFM) Fits Approx 3 to 18kg
Extra Inserts
Wetbags
Bamboo Biodegradable liners

The Materials used and features:
All in 2 Nappy (AI2):
Outer Shell Features- A waterproof TPU shell to keep all the wetness in.
Lining is a made of Microfleece material which is soft on baby's skin and Wicks moisture away from the baby's skin it is also very fast drying
Double leg Gussets to avoids any potential side leg Leaks
a poo guard at the back to reduce any leaks from occurring up the back
Insert is Made from 70% Bamboo and 30% Organic Cotton, The extra trim insert with extra absorbency qualities that can easily be double up for a heavy wetting baby or for an all night solution.

Insert snaps in and out Which is easy to remove and replace
A Pocket opening is also available to add a Booster in for long naps or for night time use. Insert is 2 layers sewn together and then folded twice to create 6 layers of absorbency. Unsnap insert from shell for washing, As there is not 3 layers sewn together like most inserts, it dries much quicker and washes more thoroughly, therefore less chance of smells accumulating

Why are these inserts so great?
– Super soft and silky
– Very breathable
– Naturally Anti-bacterial
– Absorbs 3 to 4 times more than cotton
– Doesn't feel sticky or uncomfortable when wet

The newborn nappy has a TPU waterproof Shell and is a all in one (AIO), has 4 layers of absorbency of 70% Bamboo and 30% Organic Cotton, With Microfleece lining which is super soft on newborns delicate skin.
The newborn nappy has a snap to hold down the front of the nappy where the umbilical cord will be for the first week or so. there is also snaps to adjust the size that little bit smaller for Premature babies or small babies. There is also double leg gussets to avoid any leaks around the legs. There is also a Poo guard at the back to avoid any leaks coming up from the back. The waist has a cross over snap for a extra small waist

PRICING:
One Size Fits Most:
Velcro: $25.95
Snap: $25.95
All In One Newborn:
$19.95

PACKAGES:
Price Depends on What nappies you choose for your package

Trial 3 pack: 5% Discount
6 Pack: 10% Discount
12 Pack: 15% Discount
24 Pack: 20% discount

Extra Inserts $7.00
Wetbags: $10
Bamboo Biodegradable Liners: $10
Contact Details:
Lorna Whitcombe
Phone: 0437816204
E-mail: willowdapplezbubs@fernmail.example
Bubsbook: www.bubsbook.example/WillowDapplezBubs
Updates

I have changed a few things on the brief so please read carefully before changing or making another design,

Thanks :) 

Target Market(s)

Mums and Dads, care takers, Guardians and grandparents

Industry/Entity Type

Baby

Requirements
Must have
• Must have the Logo and picture i have sent but you are welcome to put other pictures of babies but please do not put pictures of babies with disposable nappies on. and if you are going to put pics of babies i would prefer the pictures not to show how the Velcro or snaps look at the front of the nappy. for example: put pictures that show the nappy side on or from the back. You could put pictures of babies or of nature etc "saving the Environment"
Should not have
• no pictures of other cloth nappy brands No disposable nappies

```html
<!DOCTYPE html>
<html lang="en">
<head>
<meta charset="utf-8">
<title>Willow Dapplez Nappies – Brochure</title>
<link rel="stylesheet" href="https://fonts.googleapis.com/css2?family=Arimo:wght@400;700&family=Montserrat:wght@800&family=Fira+Sans:wght@400&display=swap">
<style>
  :root{
    --plum:#923f74;
    --plum-text:#9a3f7a;
    --page:#e6e6e6;
    --white:#ffffff;
    --photo-cool:#dfe6ef;
    --photo-warm:#f1d3c3;
    --photo-cream:#f7ebe2;
  }
  *{box-sizing:border-box;margin:0;padding:0}
  html,body{width:859px;height:1200px;overflow:hidden;background:var(--page)}
  body{font-family:"Arimo",Arial,sans-serif;color:var(--white)}
  .canvas{position:relative;width:859px;height:1200px}

  .spread{position:absolute;left:43px;width:773px}
  .spread--outside{top:44px;height:545px;background:var(--white)}
  .spread--inside{top:610px;height:559px;background:var(--plum);overflow:hidden}

  .why-panel{position:absolute;left:0;top:0;width:258px;height:545px;background:var(--plum);padding:40px 18px 0 23px}
  .why-panel h2{font-family:"Montserrat",Arial,sans-serif;font-weight:800;font-size:19px;letter-spacing:.2px;margin-bottom:29px}
  .why-panel p{font-size:10px;line-height:12.6px;text-align:justify}

  .hero-photo{position:absolute;left:258px;top:0;width:515px;height:287px;
    background:linear-gradient(160deg,var(--photo-cool) 0%,#f3f1f2 45%,var(--photo-warm) 100%)}
  .motto{position:absolute;left:581px;top:24px;font-family:"Fira Sans",Arial,sans-serif;font-size:20px;line-height:24px;color:var(--plum-text)}

  .contact{position:absolute;left:277px;top:341px;font-size:11px;line-height:13px;color:var(--plum-text)}
  .contact p{margin-bottom:13px}

  .brand-mark{position:absolute;left:540px;top:354px;width:220px;text-align:center;color:var(--plum-text)}
  .brand-mark .dot{display:block;width:86px;height:86px;border-radius:50%;background:var(--plum);margin:0 auto 16px}
  .brand-mark .name{font-size:19px;font-weight:400}
  .origin{position:absolute;left:541px;top:506px;width:220px;text-align:center;font-size:9.5px;line-height:12px;color:var(--plum-text)}

  .col-main{position:absolute;left:23px;top:40px;width:500px}
  .col-side{position:absolute;left:539px;top:40px;width:215px}
  h3{font-family:"Arimo",Arial,sans-serif;font-weight:700;font-size:12px;text-transform:uppercase;margin-bottom:2px}
  .copy{font-size:9.7px;line-height:11.6px}
  .copy b{font-weight:700}
  .section{margin-bottom:13px}
  .newborn{margin-top:21px}

  .inside-photo{position:absolute;right:0;bottom:0;width:773px;height:559px}
</style>
</head>
<body>
<div class="canvas">

  <section class="spread spread--outside">
    <div class="why-panel">
      <h2>WHY USE CLOTH?</h2>
      <p>-Save thousands of Dollars<br>-Easy to use<br>-Looks Cute<br>-Super Absorbency<br>
      It costs approximately $3000 to use disposable nappies on a child from birth until 2 and a half years, that is Approximately 6000 nappies going into Landfill. This is based on a child going through 6-8 nappies per day.<br>
      Modern cloth nappies, on the other hand, cost around $500 for a full stash of 24 nappies. This allows for the child to wear 6-8 nappies per day with a load of nappies going in the wash every 2-3 days. As we have a range of nappies that are one-size-fits-most for bubs ranging from 3kg to 18kg, that $500 would cover your complete stash from birth right through to toilet training, Not to mention the money you would save by using the nappies again for any subsequent Children you may have.<br>
      Eliminates your baby's exposure to harmful Chemicals that can be in disposable nappies.<br>
      The manufacturing and use of disposable nappies can amount to 2-3 times more wasted water than using cloth nappies.<br>
      Using Disposable Nappies fill up our landfill, Disposable nappies take more than 100 years to decompose, possibly up to 500 years.</p>
    </div>

    <div class="hero-photo" role="img" aria-label="Photo of a sleeping baby wrapped in a soft white towel"></div>
    <p class="motto">Cloth Nappies<br>The Modern Way</p>

    <div class="contact">
      <p>Contact Details</p>
      <p>Lorna Whitcombe</p>
      <p>Phone:<br>0437816204</p>
      <p>E-mail:<br>willowdapplezbubs@fernmail.example</p>
      <p>Bubsbook:<br>www.bubsbook.example/WillowDapplezBubs</p>
    </div>

    <div class="brand-mark">
      <span class="dot"></span>
      <span class="name">Willow Dapplez</span>
    </div>
    <p class="origin">The nappy design is designed in Australia and Australian Owned.</p>
  </section>

  <section class="spread spread--inside">
    <svg class="inside-photo" viewBox="0 0 773 559" role="img" aria-label="Photo of a smiling baby lying on a soft white rug">
      <defs>
        <linearGradient id="warmTone" x1="0" y1="0" x2="1" y2="1">
          <stop offset="0" stop-color="#f7f3f0"/>
          <stop offset=".55" stop-color="#f1d7c6"/>
          <stop offset="1" stop-color="#f7ebe2"/>
        </linearGradient>
      </defs>
      <path d="M513 559 C518 380 620 254 773 240 L773 559 Z" fill="url(#warmTone)"/>
    </svg>

    <div class="col-main">
      <div class="section">
        <h3>Products Available</h3>
        <p class="copy"><b>Newborn</b> - All in One (AIO) Fits approx 2-7kg<br>
        <b>Velcro</b> - All in Two, One size Fits Most (OSFM) fits approx 3 to 18kg<br>
        <b>Snap</b> - All in Two, One size Fits Most (OSFM) Fits Approx 3 to 18kg<br>
        <b>Extra Inserts, Wetbags and Bamboo Biodegradable liners</b></p>
      </div>
      <div class="section">
        <h3>The Materials Used and Features</h3>
        <p class="copy">All in 2 Nappy (Ai2):<br>
        Outer Shell Features- A waterproof TPU shell to keep all the wetness in.<br>
        Lining is a made of Microfleece material which is soft on baby's skin and Wicks moisture away from the baby's skin it is also very fast drying<br>
        Double leg Gussets to avoids any potential side leg Leaks<br>
        a poo guard at the back to reduce any leaks from occurring up the back<br>
        Insert is Made from 70% Bamboo and 30% Organic Cotton, The extra trim insert with extra absorbency qualities that can easily be double up for a heavy wetting baby or for an all night solution.<br>
        Insert snaps in and out Which is easy to remove and replace<br>
        A Pocket opening is also available to add a Booster in for long naps or for night time use. Insert is 2 layers sewn together and then folded twice to create 6 layers of absorbency. Unsnap insert from shell for washing. As there is not 3 layers sewn together like most inserts, it dries much quicker and washes more thoroughly, therefore less chance of smells accumulating</p>
      </div>
      <div class="section">
        <h3>Why Are These Inserts So Great?</h3>
        <p class="copy">– Super soft and silky<br>– Very breathable<br>– Naturally Anti-bacterial<br>– Absorbs 3 to 4 times more than cotton<br>– Doesn't feel sticky or uncomfortable when wet</p>
        <p class="copy newborn">The newborn nappy has a TPU waterproof Shell and is a all in one (AIO), has 4 layers of absorbency of 70% Bamboo and 30% Organic Cotton, With Microfleece lining which is super soft on newborns delicate skin.<br>
        The newborn nappy has a snap to hold down the front of the nappy where the umbilical cord will be for the first week or so. there is also snaps to adjust the size that little bit smaller for Premature babies or small babies. There is also double leg gussets to avoid any leaks around the legs. There is also a Poo guard at the back to avoid any leaks coming up from the back. The waist has a cross over snap for a extra small waist</p>
      </div>
    </div>

    <div class="col-side">
      <div class="section">
        <h3>Pricing</h3>
        <p class="copy"><b>One Size Fits Most:<br>Velcro: $25.95<br>Snap: $25.95<br>All In One Newborn: $19.95</b></p>
      </div>
      <div class="section">
        <h3>Packages</h3>
        <p class="copy">Price Depends on What nappies you choose for your package<br>
        <b>Trial 3 pack: 5% Discount<br>6 Pack: 10% Discount<br>12 Pack: 15% Discount<br>24 Pack: 20% discount</b></p>
        <p class="copy" style="margin-top:12px"><b>Extra Inserts $7.00<br>Wetbags: $10<br>Bamboo Biodegradable Liners: $10</b></p>
      </div>
    </div>
  </section>

</div>
</body>
</html>
```